Bright Harbor Design

We need a web design for our startup company based in Zurich, Switzerland called Bright Harbor. We offer professional flirt and dating advice, self development with seminars and practical coachings.

The final website aims for two capital goals. First, it will contain text, pictures and video based content presenting and advertising our services. Furthermore, we want to bind our costumers with a plattform offering them to share their expiriences related with our services.

The targeted group will be men from 25 to 40 years.
Updates

The design requires also a register-box to put in the clients Name and Email

I need (besides of the "email registration box") a "Video Gallery", "Blog" and "Agenda (with the next events to come)"

Target Market(s)

Guys around 25 to 40 years who want to improve their social lifestyle

Industry/Entity Type

Advertising

Requirements
Must have
• First and foremost, the design must transfer strong emotions and suggest an attractive social lifestyle.

The design should not be overloaded with content but should include pictures, videos and text.

The design should present a modern, urban lifestyle.
Nice to have
• There is a logo attached to the assignement. However, if you have a good idea for an improved or different logo, please do not hesitate to design your ideas.

```html
<!DOCTYPE html>
<html lang="en">
<head>
<meta charset="utf-8">
<title>Bright Harbor</title>
<link rel="stylesheet" href="https://fonts.googleapis.com/css2?family=Montserrat:wght@400;500;600;700&family=Open+Sans:wght@300;400;600;700&display=swap">
<style>
:root{
  --navy:#17284a;
  --olive:#6f7a45;
  --olive-tile:#767e4d;
  --rust:#5e1c0f;
  --amber:#98611e;
  --amber-text:#8e5b1f;
  --teal:#5f7b76;
  --ink:#1b1b1b;
  --body:#555;
  --rule:#e2e2e2;
  --field:#f3f3f3;
  --chip:#e6e6e6;
}
*{box-sizing:border-box;margin:0;padding:0}
html,body{width:1200px;height:1114px;overflow:hidden;background:#fff}
.page{position:relative;width:1400px;height:1300px;transform:scale(.857143);transform-origin:0 0;font-family:"Open Sans",sans-serif;color:var(--ink)}
.abs{position:absolute}
.brand{left:148px;top:58px;display:flex;align-items:center;gap:14px;font-family:"Montserrat",sans-serif;font-weight:700;font-size:34px;color:var(--navy);letter-spacing:.5px}
.brand-dot{width:44px;height:44px;border-radius:50%;background:var(--navy)}
.auth{top:18px;right:143px;display:flex;gap:7px}
.btn{display:inline-flex;align-items:center;justify-content:center;font-family:"Montserrat",sans-serif;font-weight:600;color:#fff;text-decoration:none}
.auth .btn{height:39px;padding:0 21px;font-size:14px;border-radius:3px}
.btn-signup{background:var(--olive)}
.btn-signin{background:#000}
.nav{top:100px;right:141px;display:flex;gap:38px;font-family:"Montserrat",sans-serif;font-weight:500;font-size:16px;letter-spacing:2.4px}
.hero-title{left:147px;top:203px;font-family:"Montserrat",sans-serif;font-weight:500;font-size:41px;line-height:43px;color:var(--olive)}
.hero-rule{left:149px;top:302px;width:267px;height:1px;background:#ccc}
.hero-lede{left:147px;top:321px;width:252px;font-size:19px;line-height:30px;letter-spacing:.3px}
.btn-how{left:149px;top:434px;width:187px;height:42px;background:var(--rust);font-size:13px;letter-spacing:3px;border-radius:2px}
.hero-photo{left:420px;top:145px;width:520px;height:395px;background:radial-gradient(ellipse at 55% 45%,#c99a7c 0%,#d9b69f 35%,#eee6df 65%,#fff 82%)}
.promo{left:902px;width:356px;height:157px;border-radius:38px 0 38px 0;display:flex;align-items:center;justify-content:center;text-align:center;font-family:"Montserrat",sans-serif;font-weight:500;font-size:18px;line-height:29px;color:#fff;padding:0 50px}
.promo-game{top:174px;background:linear-gradient(135deg,#8a3e2a 0%,#b06a4e 55%,#9a5038 100%)}
.promo-share{top:355px;background:linear-gradient(135deg,#7d7a45 0%,#9b9358 50%,#7a7a44 100%)}
.tiles{top:558px;left:148px;display:flex;gap:22px}
.tile{width:356px;height:87px;border-radius:3px;display:flex;align-items:center;justify-content:center;gap:18px;color:#fff;font-family:"Montserrat",sans-serif;font-weight:700;font-size:16px;letter-spacing:8px}
.tile-blog{background:var(--amber)}
.tile-agenda{background:var(--olive-tile)}
.tile-videos{background:var(--teal)}
.tile-icon{width:56px;height:56px;border-radius:50%;background:#fff;box-shadow:0 0 0 5px rgba(255,255,255,.35);display:flex;align-items:center;justify-content:center}
.section-title{font-family:"Montserrat",sans-serif;font-weight:500;font-size:28px;color:var(--amber-text)}
.section-sub{font-size:15px;color:#333;margin-top:2px}
.connections{left:148px;top:698px;width:700px}
.btn-share{position:absolute;right:0;top:18px;height:34px;padding:0 19px;background:var(--chip);color:#222;font-size:11px;letter-spacing:3px;font-weight:600}
.story{font-size:15.5px;line-height:27px;color:var(--body);font-weight:300;width:695px}
.story a{color:var(--amber-text);font-weight:700;font-size:13px;text-decoration:none;margin-left:4px}
.story-list{margin-top:31px}
.story + .story{border-top:1px solid var(--rule);margin-top:18px;padding-top:16px}
.register{left:902px;top:698px;width:356px}
.field-label{display:block;font-size:17px;font-weight:300;color:#444;margin-top:30px}
.field-label:first-of-type{margin-top:38px}
.field{height:38px;background:var(--field);border:1px solid #e4e4e4;margin-top:7px}
.pw{display:flex;justify-content:space-between}
.pw .field{width:166px}
.reg-actions{display:flex;justify-content:space-between;align-items:center;margin-top:26px}
.check{display:flex;align-items:center;gap:10px;font-size:13px}
.check span{width:16px;height:16px;border:1px solid #aaa;border-radius:2px}
.btn-signme{width:163px;height:34px;background:var(--rust);font-size:12px;letter-spacing:3px}
.privacy{margin-top:24px;font-size:12.5px;color:#555;text-align:right;font-weight:600;white-space:nowrap;direction:rtl}
.privacy span{direction:ltr;unicode-bidi:embed}
.footer-rule{left:149px;top:1176px;width:1096px;height:1px;background:var(--rule)}
.footer-brand{left:150px;top:1210px;display:flex;align-items:center;gap:10px;font-family:"Montserrat",sans-serif;font-weight:700;font-size:20px;color:#999}
.footer-brand .brand-dot{width:26px;height:26px;background:#999}
.legal{right:143px;top:1228px;font-size:13px}
.legal span{margin:0 5px}
</style>
</head>
<body>
<div class="page">
  <header>
    <div class="abs brand"><span class="brand-dot"></span>Bright Harbor</div>
    <div class="abs auth"><a class="btn btn-signup" href="#">SIGN UP</a><a class="btn btn-signin" href="#">SIGN IN</a></div>
    <nav class="abs nav"><span>HOW IT WORKS</span><span>CONNECTIONS</span><span>VIDEOS</span><span>CONTACT US</span></nav>
  </header>

  <section class="hero">
    <h1 class="abs hero-title">BRIGHT<br>HARBOR</h1>
    <div class="abs hero-rule"></div>
    <p class="abs hero-lede">It’s exactly what you need to get your social life back on track.</p>
    <a class="abs btn btn-how" href="#">HOW IT WORKS</a>
    <div class="abs hero-photo" role="img" aria-label="Smiling couple embracing outdoors by the sea"></div>
    <div class="abs promo promo-game" role="img" aria-label="Warm-toned city bar scene behind the text">HOW CAN BRIGHT HARBOR GET YOU BACK IN THE GAME?</div>
    <div class="abs promo promo-share" role="img" aria-label="Olive-toned shop interior behind the text">SHARE SOME OF YOUR BRIGHT HARBOR MEMORIES WITH US.</div>
  </section>

  <div class="abs tiles">
    <div class="tile tile-blog"><span class="tile-icon"><svg width="26" height="24" viewBox="0 0 26 24"><ellipse cx="13" cy="10" rx="12" ry="9" fill="#98611e"/><path d="M6 16 L4 23 L12 18Z" fill="#98611e"/></svg></span>THE BLOG</div>
    <div class="tile tile-agenda"><span class="tile-icon"><svg width="26" height="24" viewBox="0 0 26 24"><rect x="1" y="3" width="24" height="20" rx="2" fill="#767e4d"/><rect x="6" y="0" width="3" height="6" fill="#767e4d"/><rect x="17" y="0" width="3" height="6" fill="#767e4d"/><g fill="#fff"><rect x="4" y="9" width="4" height="3"/><rect x="11" y="9" width="4" height="3"/><rect x="18" y="9" width="4" height="3"/><rect x="4" y="15" width="4" height="3"/><rect x="11" y="15" width="4" height="3"/><rect x="18" y="15" width="4" height="3"/></g></svg></span>OUR AGENDA</div>
    <div class="tile tile-videos"><span class="tile-icon"><svg width="22" height="26" viewBox="0 0 22 26"><path d="M3 1 L21 13 L3 25Z" fill="#5f7b76"/></svg></span>BH VIDEOS</div>
  </div>

  <section class="abs connections">
    <h2 class="section-title">CONNECTIONS</h2>
    <p class="section-sub">Past users Bright Harbor expereinces</p>
    <a class="btn btn-share" href="#">SHARE WITH US</a>
    <div class="story-list">
      <p class="story">Lorem ipsum dolor sit amet, consectetur adipisicing elit, sed do eiusmod tempor incididunt ut labore et dolore magna aliqua. Ut enim ad minim veniam, quis nostrud exercitation ullamco laboris nisi ut aliquip ex ea commodo consequat. Duis aute irure dolor in reprehenderit in voluptate velit esse cillum dolore eu fugiat nulla pariatur. <a href="#">READ MORE</a></p>
      <p class="story">Lorem ipsum dolor sit amet, consectetur adipisicing elit, sed do eiusmod tempor incididunt ut labore et dolore magna aliqua. Ut enim ad minim veniam, quis nostrud exercitation ullamco laboris nisi ut aliquip ex ea commodo consequat. Duis aute irure dolor in reprehenderit. <a href="#">READ MORE</a></p>
      <p class="story">Lorem ipsum dolor sit amet, consectetur adipisicing elit, sed do eiusmod tempor incididunt ut labore et dolore magna aliqua. Ut enim ad minim veniam, quis nostrud exercitation ullamco laboris nisi ut aliquip ex ea commodo consequat. <a href="#">READ MORE</a></p>
    </div>
  </section>

  <section class="abs register">
    <h2 class="section-title">REGISTER</h2>
    <p class="section-sub">It’s easy &amp; free to register, why not!</p>
    <label class="field-label">Name</label>
    <div class="field"></div>
    <label class="field-label">Email</label>
    <div class="field"></div>
    <label class="field-label">Password</label>
    <div class="pw"><div class="field"></div><div class="field"></div></div>
    <div class="reg-actions">
      <label class="check"><span></span>Receive Newsletter</label>
      <a class="btn btn-signme" href="#">SIGN ME UP</a>
    </div>
    <p class="privacy"><span>We respect your privacy &amp; will not share your infomation.</span></p>
  </section>

  <footer>
    <div class="abs footer-rule"></div>
    <div class="abs footer-brand"><span class="brand-dot"></span>Bright Harbor</div>
    <p class="abs legal">© Bright Harbor<span>|</span>Privacy Policy<span>|</span>Terms of Use</p>
  </footer>
</div>
</body>
</html>
```